Bright Harbor Counseling Letterhead for hip modern business

I would like some ombre use of the colors in the logo hip letterhead that incorporates logo colors and feel, needs to connect with young professionals and college students. i need to be able to write letters to schools to excuse absences as well. i like color blocks on one side preferably using colors from the attached logo design.

Target Market(s)

high income young people, young adults and college students

Industry/Entity Type

mental health

Font styles to use
Serif
Sans Serif

Colors
0054AA
0677BA
7BADD7
CADEEF
E8F1F8
0094D4
00A9DD
6FCCEA
C7EBF8
E9F6FB
00AB8E
00BBA5
67D7C9
C6EFE9
E9F9F6
59FF00
82FF00
B8FF75
E3FFCB
F4FFEA
A7469A
B969AE
D3A5CF
EDDBEB
F8F0F9
6B429C
8869AF
B7A5CE
E3DAEB
F3F0F8

Requirements
Must have
• a modern hip feel, somewhat color

```html
<!DOCTYPE html>
<html lang="en">
<head>
<meta charset="utf-8">
<title>Bright Harbor Counseling Letterhead</title>
<link href="https://fonts.googleapis.com/css2?family=Open+Sans:wght@300;400;600&display=swap" rel="stylesheet">
<style>
  :root {
    --backdrop: #d5d9db;
    --paper: #ffffff;
    --ink: #4a4a4a;
    --ink-soft: #6d6d6d;
    --accent-blue: #1f7cc4;
    --plum: #a7469a;
    --plum-deep: #97306f;
    --sky: #6cc6ec;
    --rule: #8c8c8c;
    --tint-lilac: #efe8f3;
    --tint-sky: #e6f4fb;
    --tint-rose: #f6e6ee;
  }
  * { box-sizing: border-box; margin: 0; padding: 0; }
  html, body { width: 1200px; height: 784px; overflow: hidden; }
  body {
    background: var(--backdrop);
    font-family: "Open Sans", Arial, sans-serif;
    position: relative;
  }
  .letterhead {
    position: absolute;
    left: 320px; top: 30px;
    width: 560px; height: 724px;
    background: var(--paper);
    box-shadow: 0 6px 18px rgba(0,0,0,0.18);
    overflow: hidden;
  }
  .brand {
    position: absolute;
    top: 44px; right: 40px;
    display: flex; align-items: center; gap: 10px;
  }
  .brand-name {
    font-weight: 300;
    font-size: 22px;
    color: var(--ink);
    letter-spacing: 0.2px;
  }
  .brand-dot {
    width: 22px; height: 22px;
    border-radius: 50%;
    background: var(--plum);
  }
  .contact {
    position: absolute;
    top: 104px; right: 40px;
    text-align: right;
    font-size: 9.5px;
    line-height: 15px;
  }
  .contact-address { color: var(--accent-blue); font-weight: 600; }
  .contact-lines { color: var(--ink-soft); }
  .contact-item { display: inline-flex; align-items: center; gap: 3px; margin-left: 6px; }
  .contact-item svg { width: 8px; height: 8px; }
  .contact-rule {
    position: absolute;
    top: 142px; right: 40px;
    width: 300px; height: 2px;
    background: var(--rule);
  }
  .contact-rule-end {
    position: absolute;
    top: 139px; right: 34px;
    width: 8px; height: 8px;
    background: var(--accent-blue);
  }
  .tint-field {
    position: absolute;
    top: 170px; right: 0;
    width: 180px; height: 150px;
    background: linear-gradient(135deg, var(--tint-sky) 0%, var(--tint-lilac) 55%, var(--tint-rose) 100%);
    opacity: 0.8;
  }
  .corner-sweep {
    position: absolute;
    left: 0; bottom: 0;
  }
</style>
</head>
<body>
  <main class="letterhead">
    <div class="brand">
      <span class="brand-dot"></span>
      <span class="brand-name">Bright Harbor Counseling</span>
    </div>

    <div class="contact">
      <div class="contact-address">120 Harbor Lane, Ste 40, Oregon, 97201, United States</div>
      <div class="contact-lines">
        <span class="contact-item"><svg viewBox="0 0 10 10"><circle cx="5" cy="5" r="4.5" fill="none" stroke="#1f7cc4"/></svg>(000) 000-0000</span>
        <span class="contact-item"><svg viewBox="0 0 10 10"><circle cx="5" cy="5" r="5" fill="#1f7cc4"/></svg>(000) 000-0000</span>
        <span class="contact-item"><svg viewBox="0 0 10 10"><rect x="0.5" y="2" width="9" height="6" fill="#1f7cc4"/></svg>info@brightharbor.com</span>
        <span class="contact-item"><svg viewBox="0 0 10 10"><circle cx="5" cy="5" r="5" fill="#7badd7"/></svg>www.brightharbor.com</span>
      </div>
    </div>
    <div class="contact-rule"></div>
    <div class="contact-rule-end"></div>

    <div class="tint-field" role="img" aria-label="Soft pastel colour-block decoration in sky, lilac and rose tints"></div>

    <svg class="corner-sweep" width="260" height="290" viewBox="0 0 260 290" role="img" aria-label="Curved corner colour sweep fading from plum to sky blue">
      <defs>
        <linearGradient id="sweep-fade" x1="0" y1="1" x2="1" y2="0">
          <stop offset="0" stop-color="#97306f"/>
          <stop offset="0.55" stop-color="#b969ae"/>
          <stop offset="1" stop-color="#6cc6ec"/>
        </linearGradient>
      </defs>
      <path d="M0,0 C40,90 120,130 185,170 C225,195 240,250 242,290 L0,290 Z" fill="url(#sweep-fade)"/>
    </svg>
  </main>
</body>
</html>
```